Design the 21st Golden Reel Indie Screen Week Poster. Think modern, chic, cool, film, movies - driving people to the film festival - the film festivla is in San Francisco and the SF East Bay. Our logo is attached. Dates will be determined soon . please use - November 2 - 11, 2018 (for placement) Keep in mind abstract, chic, modern - eye catching. website is www.grisw.example

Target Market(s)

25 - 45 year old - upper middle class

Industry/Entity Type

Film Production

Colors

Designer to choose colors to be used in the design.

Requirements
Must have
• logo (attached) www.grisw.example - chic modern design
Nice to have
• best coolest poster ever!
Should not have
• CLIP ART!!!

```html
<!DOCTYPE html>
<html lang="en">
<head>
<meta charset="utf-8">
<title>21st Golden Reel Indie Screen Week</title>
<link rel="stylesheet" href="https://fonts.googleapis.com/css2?family=Alfa+Slab+One&family=Quicksand:wght@400;700&display=swap">
<style>
  :root {
    --title-yellow: #ece53c;
    --date-cream: #f6efe6;
    --copy-white: #ffffff;
    --mark-lime: #98c93c;
    --lens-black: #120814;
    --lens-plum: #3a1230;
    --paint-magenta: #b0306e;
    --paint-violet: #5a3fc0;
    --paint-cyan: #7ad0e8;
    --paint-yellow: #f1ec86;
    --haze: #f4f6f0;
  }
  * { margin: 0; padding: 0; box-sizing: border-box; }
  html, body { width: 776px; height: 1200px; overflow: hidden; background: var(--lens-black); }
  .poster { position: relative; width: 776px; height: 1200px; overflow: hidden; }
  .poster__backdrop {
    position: absolute; inset: 0;
    background:
      radial-gradient(ellipse 260px 230px at 380px 880px, var(--lens-black) 0%, #2a1024 55%, transparent 100%),
      radial-gradient(ellipse 420px 380px at 380px 860px, var(--lens-plum) 0%, #4a1838 60%, transparent 100%),
      radial-gradient(ellipse 200px 140px at 170px 330px, rgba(176,48,110,.55), transparent 100%),
      radial-gradient(ellipse 260px 300px at 60px 760px, rgba(90,63,192,.85), transparent 100%),
      radial-gradient(ellipse 240px 200px at 720px 460px, rgba(90,63,192,.55), transparent 100%),
      radial-gradient(ellipse 260px 120px at 420px 90px, rgba(241,236,134,.7), transparent 100%),
      radial-gradient(ellipse 300px 160px at 250px 180px, rgba(122,208,232,.65), transparent 100%),
      radial-gradient(ellipse 260px 180px at 640px 220px, rgba(122,208,232,.5), transparent 100%),
      linear-gradient(180deg, var(--haze) 0%, #e6eee4 22%, #c98bb0 34%, #5a2450 46%, #2a0f28 75%, var(--lens-black) 100%);
  }
  .poster__type { position: absolute; inset: 0; width: 776px; height: 1200px; }
  .title { font-family: "Alfa Slab One", "Georgia", serif; fill: var(--title-yellow); font-size: 56px; }
  .dates { font-family: "Alfa Slab One", "Georgia", serif; fill: var(--date-cream); font-size: 42px; }
  .info { font-family: "Quicksand", "Helvetica", sans-serif; fill: var(--copy-white); font-size: 19px; font-weight: 400; }
  .info__url { font-weight: 700; }
  .brand { position: absolute; left: 585px; top: 1040px; width: 150px; text-align: center; }
  .brand__dot { display: block; width: 36px; height: 36px; margin: 0 auto 10px; border-radius: 50%; background: var(--mark-lime); }
  .brand__name { font-family: "Alfa Slab One", "Georgia", serif; font-size: 34px; line-height: 1; color: var(--copy-white); letter-spacing: 2px; }
</style>
</head>
<body>
<main class="poster">
  <div class="poster__backdrop" role="img" aria-label="Abstract photo of a camera lens in deep plum and black, washed with streaks of cyan, yellow, magenta and violet paint"></div>

  <svg class="poster__type" viewBox="0 0 776 1200" xmlns="http://www.w3.org/2000/svg">
    <defs>
      <path id="arc-title-1" d="M140,505 Q410,360 680,590"/>
      <path id="arc-title-2" d="M125,590 Q440,420 705,720"/>
      <path id="arc-title-3" d="M255,630 Q400,565 560,665"/>
      <path id="arc-dates" d="M258,695 C445,605 640,650 628,915"/>
      <path id="arc-info-1" d="M318,742 Q440,668 575,738"/>
      <path id="arc-info-2" d="M305,796 Q485,690 550,905"/>
      <path id="arc-info-3" d="M318,822 Q430,752 505,840"/>
      <path id="arc-info-4" d="M336,842 Q390,812 445,842"/>
    </defs>

    <text class="title"><textPath href="#arc-title-1" startOffset="50%" text-anchor="middle">21st Golden Reel</textPath></text>
    <text class="title"><textPath href="#arc-title-2" startOffset="50%" text-anchor="middle">Indie Screen</textPath></text>
    <text class="title"><textPath href="#arc-title-3" startOffset="50%" text-anchor="middle">Week</textPath></text>

    <text class="dates"><textPath href="#arc-dates">November 2-11, 2018</textPath></text>

    <text class="info"><textPath href="#arc-info-1">Go to <tspan class="info__url">www.grisw.example</tspan></textPath></text>
    <text class="info"><textPath href="#arc-info-2">for more information on ticket</textPath></text>
    <text class="info"><textPath href="#arc-info-3">prices, schedules</textPath></text>
    <text class="info"><textPath href="#arc-info-4">&amp; venues</textPath></text>
  </svg>

  <div class="brand">
    <span class="brand__dot"></span>
    <span class="brand__name">GRISW</span>
  </div>
</main>
</body>
</html>
```